Ledgerwise Business Card Design

Business Card Design for new business called Ledgerwise focused on selling business software to small and medium size companies who have outgrown Tallyhouse. Similar companies would be Tallyhouse, Vemo, BrightCore. Also Dealharbor would be good to look at for additional ideas around look and feel.

Target Market(s)

Business to Business

Industry/Entity Type

Information Technology

Contact Information for Business Card

Standard Business Card Information

Font styles to use
Sans Serif

```html
<!DOCTYPE html>
<html lang="en">
<head>
<meta charset="utf-8">
<title>Ledgerwise Business Card</title>
<link rel="stylesheet" href="https://fonts.googleapis.com/css2?family=Roboto+Condensed:wght@400;700&display=swap">
<style>
  :root {
    --backdrop: #e6e5e1;
    --card: #fbfbfc;
    --card-shade: #eeeff2;
    --navy: #0f4a7f;
    --orange: #ee7e12;
    --white: #ffffff;
    --faint: #e3e5ea;
  }
  * { margin: 0; padding: 0; box-sizing: border-box; }
  html, body { width: 1193px; height: 1200px; overflow: hidden; }
  body {
    background: var(--backdrop);
    position: relative;
    font-family: "Roboto Condensed", "Arial Narrow", sans-serif;
  }
  .card {
    position: absolute;
    left: 211px;
    width: 721px;
    height: 427px;
    background: var(--card);
    overflow: hidden;
  }
  .card-front { top: 158px; }
  .card-back { top: 642px; background: var(--card-shade); }

  .wordmark {
    position: absolute;
    font-weight: 700;
    color: var(--navy);
    letter-spacing: 1px;
    display: flex;
    align-items: center;
    line-height: 1;
  }
  .wordmark .mark-dot {
    border-radius: 50%;
    background: var(--orange);
    flex: none;
  }
  .card-front .wordmark { left: 124px; top: 176px; font-size: 68px; gap: 22px; }
  .card-front .mark-dot { width: 64px; height: 64px; }
  .card-back .wordmark { left: 44px; top: 94px; font-size: 52px; gap: 18px; }
  .card-back .mark-dot { width: 48px; height: 48px; }

  .back-art { position: absolute; inset: 0; }

  .holder { position: absolute; left: 43px; top: 228px; }
  .holder-name { font-size: 27px; font-weight: 700; color: var(--navy); }
  .holder-role { font-size: 17px; color: var(--navy); margin-top: 6px; }

  .contact-list {
    position: absolute;
    right: 28px;
    top: 290px;
    list-style: none;
    text-align: right;
  }
  .contact-list li {
    color: var(--white);
    font-size: 17px;
    height: 27.5px;
    display: flex;
    justify-content: flex-end;
    align-items: center;
    gap: 9px;
  }
  .contact-list svg { width: 18px; height: 18px; flex: none; }
</style>
</head>
<body>
  <section class="card card-front">
    <div class="wordmark"><span class="mark-dot"></span>Ledgerwise</div>
  </section>

  <section class="card card-back">
    <svg class="back-art" viewBox="0 0 721 427" width="721" height="427">
      <circle class="faint-disc" cx="560" cy="160" r="150" fill="var(--faint)"/>
      <path class="band-white" d="M0 305 C160 360 330 360 470 270 C560 215 650 190 721 188 L721 427 L0 427 Z" fill="var(--white)"/>
      <path class="band-navy" d="M0 325 C150 380 330 385 470 300 C570 240 650 215 721 212 L721 427 L0 427 Z" fill="var(--navy)"/>
      <path class="swoosh-upper" d="M60 340 C230 380 380 350 480 270 C570 205 650 185 721 180 L721 192 C650 196 575 218 490 282 C390 360 230 385 60 340 Z" fill="var(--orange)"/>
      <path class="swoosh-lower" d="M0 318 C120 345 260 360 400 330 C260 375 120 370 0 340 Z" fill="var(--orange)"/>
    </svg>

    <div class="wordmark"><span class="mark-dot"></span>Ledgerwise</div>

    <div class="holder">
      <p class="holder-name">Your Long Name</p>
      <p class="holder-role">Managing Director</p>
    </div>

    <ul class="contact-list">
      <li>+00 111 222 3333
        <svg viewBox="0 0 24 24" aria-hidden="true"><path fill="#fff" d="M3 8c0-3 4-4 9-4s9 1 9 4v2h-5V8H8v2H3zM6 11h12l2 8H4z"/></svg></li>
      <li>www.yourwebsite.com
        <svg viewBox="0 0 24 24" aria-hidden="true"><rect x="2" y="5" width="20" height="14" fill="#fff"/><path d="M2 5l10 8 10-8" stroke="var(--navy)" stroke-width="2" fill="none"/></svg></li>
      <li>yourname@yourwebsite.com
        <svg viewBox="0 0 24 24" aria-hidden="true"><circle cx="12" cy="12" r="9" fill="none" stroke="#fff" stroke-width="2"/><ellipse cx="12" cy="12" rx="4" ry="9" fill="none" stroke="#fff" stroke-width="2"/><path d="M3 12h18" stroke="#fff" stroke-width="2"/></svg></li>
      <li>Your Long Commercial address with code
        <svg viewBox="0 0 24 24" aria-hidden="true"><path fill="#fff" d="M12 2a7 7 0 0 1 7 7c0 5-7 13-7 13S5 14 5 9a7 7 0 0 1 7-7z"/><circle cx="12" cy="9" r="2.6" fill="var(--navy)"/></svg></li>
    </ul>
  </section>
</body>
</html>
```